KINDLEWAY: Social Media Post COVID-19 & Flu #1

- Create a similar design for a Social Media Post Image
- Attached, Logo, sample flu social media image.
- KINDLEWAY - must be included - in the colors provided (see attachment)
- Protect your community. Protect Your Elders. Stay Vaccinated. - must be include
-COVID-19 & Flu - will be stated somewhere
- image of mom and sons
-might include boarder
- inspiration at https://orvatrine.org/, and https://www.facebook.com/Orvatrine

```html
<!DOCTYPE html>
<html lang="en">
<head>
<meta charset="utf-8">
<title>KINDLEWAY — Flu &amp; COVID-19 Vaccination Campaign</title>
<link rel="stylesheet" href="https://fonts.googleapis.com/css2?family=Barlow+Condensed:wght@600&family=Barlow+Semi+Condensed:wght@600&family=Heebo:wght@900&display=swap">
<style>
  :root {
    --teal: #43a2ab;
    --rust: #b24a3c;
    --white: #ffffff;
    --frame-light: #e9ecec;
    --frame-teal: #6fb3b6;
    --photo-deep: #5a2418;
    --photo-mid: #8c3a26;
    --photo-warm: #b0583a;
  }
  html, body {
    margin: 0;
    padding: 0;
    width: 1200px;
    height: 1200px;
    overflow: hidden;
    background: var(--white);
  }
  .post {
    position: relative;
    width: 1200px;
    height: 1200px;
    overflow: hidden;
  }
  .border-pattern {
    position: absolute;
    inset: 0;
    background: linear-gradient(135deg, var(--frame-light), var(--frame-teal) 50%, var(--frame-light));
  }
  .family-photo {
    position: absolute;
    left: 37px;
    top: 37px;
    width: 1126px;
    height: 1126px;
    background:
      radial-gradient(ellipse at 55% 45%, var(--photo-warm) 0%, var(--photo-mid) 45%, transparent 80%),
      linear-gradient(180deg, var(--photo-mid) 0%, var(--photo-deep) 55%, var(--photo-mid) 100%);
  }
  .campaign-title {
    position: absolute;
    left: 79px;
    top: 79px;
    width: 730px;
    height: 187px;
    border: 8px solid var(--white);
    overflow: hidden;
  }
  .campaign-name {
    position: absolute;
    left: 0;
    right: 0;
    top: -14px;
    margin: 0;
    font-family: "Barlow Condensed", sans-serif;
    font-weight: 600;
    font-size: 166px;
    line-height: 1;
    letter-spacing: 2px;
    text-align: center;
    color: var(--teal);
    white-space: nowrap;
  }
  .campaign-tag {
    position: absolute;
    left: 125px;
    top: 254px;
    width: 648px;
    height: 50px;
    background: var(--white);
    font-family: "Barlow Semi Condensed", sans-serif;
    font-weight: 600;
    font-size: 36px;
    line-height: 50px;
    letter-spacing: 1px;
    text-align: center;
    color: var(--rust);
    white-space: nowrap;
  }
  .partner-mark {
    position: absolute;
    left: 861px;
    top: 77px;
    width: 254px;
    height: 206px;
    background: var(--white);
    display: flex;
    align-items: center;
    justify-content: center;
    gap: 10px;
  }
  .partner-mark .dot {
    width: 18px;
    height: 18px;
    background: var(--teal);
  }
  .partner-mark .partner-name {
    font-family: "Barlow Semi Condensed", sans-serif;
    font-weight: 600;
    font-size: 40px;
    letter-spacing: 1px;
    color: var(--teal);
  }
  .message {
    position: absolute;
    left: 104px;
    margin: 0;
    font-family: "Heebo", sans-serif;
    font-weight: 900;
    font-size: 87px;
    line-height: 1;
    color: var(--white);
    white-space: nowrap;
  }
  .message.community { top: 597px; }
  .message.elders { top: 762px; }
  .message.vaccinated { top: 907px; }
</style>
</head>
<body>
<main class="post">
  <div class="border-pattern" role="img" aria-label="Decorative teal and grey zigzag border pattern"></div>
  <div class="family-photo" role="img" aria-label="Photo of a smiling mother in a ribbon skirt hugged by her two sons, seated on a patterned blanket in a park with autumn trees, under a warm red tint"></div>

  <header class="campaign-title">
    <h1 class="campaign-name">KINDLEWAY</h1>
  </header>
  <div class="campaign-tag">FLU &amp; COVID -19 VACCINATION CAMPAIGN</div>

  <div class="partner-mark">
    <span class="dot"></span>
    <span class="partner-name">ORVATRINE</span>
  </div>

  <p class="message community">Protect Your Community.</p>
  <p class="message elders">Protect Your Elders.</p>
  <p class="message vaccinated">Stay Vaccinated.</p>
</main>
</body>
</html>
```